Design for a 4 screens iOS and Android app - "VelidMetra"

The app allows you to track your car gasoline refill ...
We need a design for the 4 screens of the app:
a) 1 form with 3 fields.
b) 1 simple list view
c) 1 summary view
d) 1 text page
2 "alerts" items are also to be designed.
No specific guidelines, nor logo or whatever.
It will be a free app distributed on iOS and Androïd.
We just want to make it looking nice & very usable for end users.
Target Market(s)
B2C app
Industry/Entity Type
Android

```html
<!DOCTYPE html>
<html lang="en">
<head>
<meta charset="utf-8">
<title>New Entry</title>
<link rel="stylesheet" href="https://fonts.googleapis.com/css2?family=Roboto:wght@300;400;500&display=swap">
<style>
  :root {
    --status-bar: #0f3449;
    --primary: #1d6488;
    --gold-light: #ecd010;
    --gold-mid: #d29a0c;
    --gold-dark: #b8780f;
    --white: #ffffff;
    --hint: #b4b4b4;
    --divider: #dcdcdc;
    --nav-bar: #000000;
  }
  * { margin: 0; padding: 0; box-sizing: border-box; }
  html, body { width: 675px; height: 1200px; overflow: hidden; background: var(--white); }
  body { font-family: 'Roboto', sans-serif; position: relative; }

  .status-bar {
    position: absolute; top: 0; left: 0; width: 675px; height: 45px;
    background: var(--status-bar); color: var(--white);
    display: flex; align-items: center; justify-content: flex-end; gap: 12px;
    padding-right: 17px; font-size: 23px; font-weight: 400;
  }
  .status-bar svg { display: block; }

  .app-bar {
    position: absolute; top: 45px; left: 0; width: 675px; height: 88px;
    background: var(--primary); color: var(--white);
    box-shadow: 0 2px 5px rgba(0,0,0,0.3); z-index: 2;
  }
  .app-bar .menu-icon { position: absolute; left: 33px; top: 33px; }
  .app-bar .title { position: absolute; left: 138px; top: 0; line-height: 88px; font-size: 37px; font-weight: 400; }
  .app-bar .chart-icon { position: absolute; right: 33px; top: 22px; }

  .total-band {
    position: absolute; top: 133px; left: 0; width: 675px; height: 238px;
    background: radial-gradient(circle at 0% 100%, var(--gold-light) 0%, var(--gold-mid) 35%, var(--gold-dark) 60%);
    color: var(--white); text-align: center;
  }
  .total-band .total-value {
    position: absolute; left: 0; right: 0; top: 58px;
    font-size: 94px; font-weight: 300; line-height: 1;
  }
  .total-band .unit { font-style: italic; margin-left: 18px; }

  .entry-form .field { position: absolute; left: 0; width: 675px; height: 80px; }
  .entry-form .field-icon { position: absolute; left: 33px; top: 0; color: var(--primary); }
  .entry-form .field-input {
    position: absolute; left: 134px; width: 441px; top: 0; height: 80px;
    border-bottom: 2px solid var(--divider);
    font-size: 41px; font-weight: 400; color: var(--hint);
    padding-left: 4px; line-height: 80px;
  }
  .field-liters { top: 459px; }
  .field-price { top: 594px; }
  .euro-sign { font-size: 44px; font-weight: 500; line-height: 80px; left: 34px !important; }

  .save-button {
    position: absolute; left: 68px; top: 953px; width: 540px; height: 92px;
    background: var(--primary); color: var(--white); border: none; border-radius: 3px;
    font-family: 'Roboto', sans-serif; font-size: 33px; font-weight: 400; letter-spacing: 0.5px;
    box-shadow: 0 2px 4px rgba(0,0,0,0.35);
  }

  .nav-bar {
    position: absolute; bottom: 0; left: 0; width: 675px; height: 86px;
    background: var(--nav-bar);
  }
  .nav-bar svg { position: absolute; top: 27px; }
</style>
</head>
<body>
  <div class="status-bar">
    <svg width="20" height="26" viewBox="0 0 20 26" aria-hidden="true"><path d="M10 1a9 9 0 0 0-9 9c0 7 9 15 9 15s9-8 9-15a9 9 0 0 0-9-9zm0 12.5a3.5 3.5 0 1 1 0-7 3.5 3.5 0 0 1 0 7z" fill="#fff"/></svg>
    <svg width="32" height="24" viewBox="0 0 32 24" aria-hidden="true"><path d="M16 23L0 5a24 24 0 0 1 32 0z" fill="#fff"/></svg>
    <svg width="26" height="26" viewBox="0 0 26 26" aria-hidden="true"><path d="M26 0v26H0z" fill="#fff"/></svg>
    <svg width="16" height="26" viewBox="0 0 16 26" aria-hidden="true"><rect x="5" y="0" width="6" height="3" fill="#fff"/><rect x="0" y="3" width="16" height="23" fill="#fff"/></svg>
    <span class="clock">10:55</span>
  </div>

  <header class="app-bar">
    <svg class="menu-icon" width="36" height="24" viewBox="0 0 36 24" aria-hidden="true"><rect y="0" width="36" height="3.5" fill="#fff"/><rect y="10" width="36" height="3.5" fill="#fff"/><rect y="20" width="36" height="3.5" fill="#fff"/></svg>
    <h1 class="title">New Entry</h1>
    <svg class="chart-icon" width="52" height="42" viewBox="0 0 52 42" aria-hidden="true" fill="none" stroke="#fff" stroke-width="3.5">
      <path d="M2 0v40h50"/>
      <path d="M9 32l12-14 11 9 15-20"/>
      <circle cx="47" cy="7" r="3" fill="#fff"/>
    </svg>
  </header>

  <section class="total-band">
    <div class="total-value">127,500<span class="unit">l</span></div>
  </section>

  <form class="entry-form">
    <div class="field field-liters">
      <svg class="field-icon" width="48" height="56" viewBox="0 0 48 56" aria-hidden="true" style="top:0">
        <path d="M14 6h12l-2 6H14z" fill="#1d6488"/>
        <path d="M2 20a8 8 0 0 1 8-8h22a6 6 0 0 1 6 6v36H2z" fill="#1d6488"/>
        <path d="M30 14l12-10" stroke="#1d6488" stroke-width="4" fill="none" stroke-linecap="round"/>
        <path d="M9 30l20 20M29 30L9 50" stroke="#fff" stroke-width="3.5"/>
      </svg>
      <div class="field-input">Liters</div>
    </div>
    <div class="field field-price">
      <span class="field-icon euro-sign" aria-hidden="true">€</span>
      <div class="field-input">Price</div>
    </div>
  </form>

  <button class="save-button" type="button">SAVE</button>

  <nav class="nav-bar">
    <svg style="left:135px" width="34" height="34" viewBox="0 0 34 34" aria-hidden="true"><path d="M30 3v28L4 17z" fill="none" stroke="#fff" stroke-width="3"/></svg>
    <svg style="left:321px" width="34" height="34" viewBox="0 0 34 34" aria-hidden="true"><circle cx="17" cy="17" r="14" fill="none" stroke="#fff" stroke-width="3"/></svg>
    <svg style="left:510px" width="34" height="34" viewBox="0 0 34 34" aria-hidden="true"><rect x="3" y="3" width="28" height="28" rx="2" fill="none" stroke="#fff" stroke-width="3"/></svg>
  </nav>
</body>
</html>
```